Tarnbrook Secondary College House displays

Our school has 4 new houses that are designed to promote school connectedness and school pride. Each house display should include the name of the house, a silhouette portrait of the person the house is named after and a famous quote from that person. Each house display should also promote the unique house colour. Details are included in the attached word document. I have also attached a Mark Dwyfor poster that gives some sort of idea about the look and feel we are after. The house name should be quite prominent.

Target Market(s)

Tarnbrook Secondary College has 1800 students. We are a unique school committed to a strengths based program. Our house system is designed to connect students to each other and to the school. To understand our school visit our website at www.tarnbrooksc.example.edu.au

Logo Text

We want a logo for each of our houses that has the house name on it - see the attached word document for details.

Font styles to use
Sans Serif

Colors
0792cd
00a990
fbed22
ec1f27

Requirements
Must have
• Colour- each house must include the colour it is aligned to. This is outlined in the attached word document

```html
<!DOCTYPE html>
<html lang="en">
<head>
<meta charset="utf-8">
<title>Houses of Tarnbrook Secondary College</title>
<link rel="stylesheet" href="https://fonts.googleapis.com/css2?family=Oswald:wght@400;500;600&display=swap">
<style>
  :root {
    --ink: #1d1d1b;
    --paper: #ffffff;
    --house-yellow: #fbed22;
    --house-blue: #0792cd;
    --house-teal: #00a990;
    --house-red: #ec1f27;
    --portrait-light: #8a8a8a;
    --portrait-dark: #2e2e2e;
  }
  * { margin: 0; padding: 0; box-sizing: border-box; }
  html, body { width: 848px; height: 1200px; overflow: hidden; background: var(--paper); }
  .poster {
    position: relative;
    width: 848px;
    height: 1200px;
    background: var(--paper);
    font-family: "Oswald", "Arial Narrow", sans-serif;
  }
  .sidebar {
    position: absolute;
    left: 0; top: 0;
    width: 141px; height: 1200px;
    background: var(--ink);
  }
  .sidebar-title {
    position: absolute;
    left: 70px; top: 555px;
    transform: translate(-50%, -50%) rotate(-90deg);
    white-space: nowrap;
    color: var(--paper);
    font-weight: 500;
    font-size: 50px;
    letter-spacing: 0.5px;
    text-transform: uppercase;
  }
  .school-mark {
    position: absolute;
    left: 50%; bottom: 38px;
    transform: translateX(-50%);
    display: flex;
    flex-direction: column;
    align-items: center;
    gap: 6px;
    color: var(--paper);
  }
  .school-mark-circle {
    width: 52px; height: 52px;
    border: 2px solid var(--paper);
    border-radius: 50%;
  }
  .school-mark-name {
    font-size: 12px;
    font-weight: 500;
    letter-spacing: 1px;
    text-transform: uppercase;
  }
  .house {
    position: absolute;
    left: 170px;
    width: 650px;
    height: 260px;
    box-shadow: 2px 3px 6px rgba(0,0,0,0.25);
    overflow: hidden;
  }
  .house--maroda { top: 31px; background: var(--house-yellow); }
  .house--stenway { top: 321px; background: var(--house-blue); }
  .house--walford { top: 611px; background: var(--house-teal); }
  .house--ashby { top: 900px; background: var(--house-red); }
  .house-art { position: absolute; left: 0; top: 0; width: 650px; height: 260px; }
  .house-name {
    position: absolute;
    right: 22px; top: 10px;
    display: flex;
    align-items: flex-start;
    gap: 10px;
    font-size: 62px;
    font-weight: 500;
    line-height: 1;
    color: var(--ink);
    text-transform: uppercase;
  }
  .house-name-arrow {
    width: 0; height: 0;
    margin-top: 8px;
    border-top: 7px solid transparent;
    border-bottom: 7px solid transparent;
    border-left: 12px solid var(--ink);
  }
  .house-quote {
    position: absolute;
    left: 250px; right: 40px;
    text-align: center;
    font-size: 17.5px;
    font-weight: 400;
    line-height: 28px;
    color: var(--ink);
    text-transform: uppercase;
  }
  .house--maroda .house-quote { top: 98px; left: 270px; right: 60px; }
  .house--stenway .house-quote { top: 90px; left: 240px; right: 25px; }
  .house--walford .house-quote { top: 93px; left: 250px; right: 20px; }
  .house--ashby .house-quote { top: 112px; left: 270px; right: 60px; }
</style>
</head>
<body>
<main class="poster">
  <aside class="sidebar">
    <h1 class="sidebar-title">Houses of Tarnbrook Secondary College</h1>
    <div class="school-mark">
      <span class="school-mark-circle"></span>
      <span class="school-mark-name">Tarnbrook</span>
    </div>
  </aside>

  <section class="house house--maroda">
    <svg class="house-art" viewBox="0 0 650 260" aria-hidden="true">
      <defs>
        <linearGradient id="portrait-tone" x1="0" y1="0" x2="1" y2="1">
          <stop offset="0" stop-color="#8a8a8a"/>
          <stop offset="1" stop-color="#2e2e2e"/>
        </linearGradient>
      </defs>
      <polygon points="0,0 190,0 85,260 0,260" fill="#1d1d1b"/>
      <polygon points="190,0 300,0 190,260 85,260" fill="#1d1d1b"/>
    </svg>
    <svg class="house-art" viewBox="0 0 650 260" role="img" aria-label="Black and white portrait photograph of the house namesake">
      <polygon points="0,0 185,0 80,260 0,260" fill="url(#portrait-tone)"/>
    </svg>
    <h2 class="house-name"><span class="house-name-arrow"></span>Maroda</h2>
    <p class="house-quote">“I laid in bed thinking about<br>the future. How I would like it to be,<br>even if I am not there.”</p>
  </section>

  <section class="house house--stenway">
    <svg class="house-art" viewBox="0 0 650 260" aria-hidden="true">
      <polygon points="190,0 290,0 180,260 80,260" fill="#1d1d1b"/>
    </svg>
    <svg class="house-art" viewBox="0 0 650 260" role="img" aria-label="Black and white portrait photograph of the house namesake">
      <polygon points="0,0 195,0 85,260 0,260" fill="url(#portrait-tone)"/>
    </svg>
    <h2 class="house-name"><span class="house-name-arrow"></span>Stenway</h2>
    <p class="house-quote">“I love life. There’s always something<br>to overcome, new people to meet… You’ve<br>just got to find your bliss and go after it.<br>That’s where the drive is, that’s how you<br>find your special place.”</p>
  </section>

  <section class="house house--walford">
    <svg class="house-art" viewBox="0 0 650 260" aria-hidden="true">
      <polygon points="190,0 290,0 180,260 80,260" fill="#1d1d1b"/>
    </svg>
    <svg class="house-art" viewBox="0 0 650 260" role="img" aria-label="Black and white portrait photograph of the house namesake in flying cap and goggles">
      <polygon points="0,0 195,0 85,260 0,260" fill="url(#portrait-tone)"/>
    </svg>
    <h2 class="house-name"><span class="house-name-arrow"></span>Walford</h2>
    <p class="house-quote">“As a small child I used to dream I could<br>fly. I could dream I could lift myself up<br>over the telegraph poles when the lions<br>and tigers were chasing me in my childish<br>nightmares”</p>
  </section>

  <section class="house house--ashby">
    <svg class="house-art" viewBox="0 0 650 260" aria-hidden="true">
      <polygon points="190,0 290,0 180,260 80,260" fill="#1d1d1b"/>
    </svg>
    <svg class="house-art" viewBox="0 0 650 260" role="img" aria-label="Black and white historical portrait photograph of the house namesake">
      <polygon points="0,0 195,0 85,260 0,260" fill="url(#portrait-tone)"/>
    </svg>
    <h2 class="house-name"><span class="house-name-arrow"></span>Ashby</h2>
    <p class="house-quote">“Poor eyes limit your sight.<br>Poor vision limits your deeds.”</p>
  </section>
</main>
</body>
</html>
```